Annual review for The Heron Collective

The Heron Collective is a small public relations agency in London specialising in corporate and public affairs. Most of our work is international and we have a strong connection to South Africa. We would like to prepare a short annual review for 2016. The review will serve as both a review of our activities in 2016, and as a credentials document. Content then will include:
1. An introduction to the business
2. Who we are
3. Projects and clients undertaken in 2016
4. News and views
We imagine it will be used mostly as a pdf but would like it to be suitable for print. We envisage it to be about 8 pages long. The design look and feel should convey a business, while small, of stature. We shall include some of our client logos but we would welcome the use of some photography / imagery to have visual impact (although we don't have very much of our own!). The corporate look and feel is white, grey and black.

Industry/Entity Type

Public Relation

Font styles to use
Sans Serif

Requirements
Must have
• My project must convey a business with flair and gravitas, that punches above its weight.
Nice to have
• Thoughtful use of imagery.

```html
<!DOCTYPE html>
<html lang="en">
<head>
<meta charset="utf-8">
<title>The Heron Collective — Short Annual Review 2016</title>
<link rel="stylesheet" href="https://fonts.googleapis.com/css2?family=Montserrat:wght@600&family=Oswald:wght@500&family=Open+Sans:wght@400&display=swap">
<style>
  :root {
    --stage: #5a5a5a;
    --paper: #f4f4f4;
    --paper-shade: #d9d9d9;
    --ink: #121212;
    --charcoal: #2a2a2a;
    --slate: #4a4a4a;
    --mist: #8c8c8c;
    --white: #ffffff;
  }
  html, body {
    margin: 0;
    width: 1200px;
    height: 789px;
    overflow: hidden;
    background: var(--stage);
  }
  .spread {
    position: absolute;
    left: 105px;
    top: 45px;
    width: 990px;
    height: 700px;
    display: flex;
    box-shadow: 0 12px 30px rgba(0,0,0,.45);
  }
  .page { width: 495px; height: 700px; display: block; }
  .brand { font-family: "Montserrat", sans-serif; font-weight: 600; }
  .heading { font-family: "Oswald", sans-serif; font-weight: 500; }
  .body { font-family: "Open Sans", sans-serif; font-weight: 400; }
</style>
</head>
<body>
<main class="spread">

  <!-- Back cover -->
  <svg class="page back-cover" viewBox="0 0 495 700" xmlns="http://www.w3.org/2000/svg">
    <defs>
      <linearGradient id="backTop" x1="0" y1="0" x2="0" y2="1">
        <stop offset="0" stop-color="#ffffff"/>
        <stop offset="1" stop-color="#d4d4d4"/>
      </linearGradient>
      <linearGradient id="backBody" x1="0" y1="0" x2="1" y2="1">
        <stop offset="0" stop-color="#3a3a3a"/>
        <stop offset="1" stop-color="#1a1a1a"/>
      </linearGradient>
      <pattern id="dots" width="4" height="4" patternUnits="userSpaceOnUse">
        <circle cx="2" cy="2" r="0.9" fill="#555"/>
      </pattern>
    </defs>
    <rect width="495" height="700" fill="url(#backBody)"/>
    <rect class="back-top" width="495" height="232" fill="url(#backTop)"/>
    <rect class="dotted-strip" y="232" width="495" height="14" fill="url(#dots)"/>
    <rect class="band-dark" y="262" width="495" height="62" fill="var(--ink)"/>
    <rect class="band-mid" y="324" width="495" height="70" fill="var(--slate)" opacity=".55"/>
    <rect class="band-footer" y="620" width="495" height="80" fill="var(--ink)"/>

    <text class="heading" x="160" y="445" font-size="25" fill="var(--white)">CONTACT US</text>
    <g class="contact-list body" font-size="10" fill="#e6e6e6">
      <circle cx="168" cy="468" r="3" fill="#e6e6e6"/>
      <text x="180" y="472">Address Goes Here</text>
      <rect x="165" y="482" width="6" height="8" rx="1.5" fill="#e6e6e6"/>
      <text x="180" y="490">Phone Number Goes Here</text>
      <rect x="164" y="500" width="9" height="7" fill="#e6e6e6"/>
      <text x="180" y="508">Fax Number Goes Here</text>
      <rect x="164" y="518" width="9" height="7" fill="none" stroke="#e6e6e6"/>
      <text x="180" y="526">E-mail Address Goes Here</text>
    </g>

    <g class="faint-brand" fill="#555">
      <circle cx="70" cy="588" r="11" fill="none" stroke="#555" stroke-width="2"/>
      <text class="brand" x="92" y="596" font-size="22">The Heron Collective</text>
    </g>
    <text class="body" x="165" y="668" font-size="11" fill="var(--mist)">www.websiteaddress.com</text>
  </svg>

  <!-- Front cover -->
  <svg class="page front-cover" viewBox="0 0 495 700" xmlns="http://www.w3.org/2000/svg">
    <defs>
      <linearGradient id="frontPaper" x1="0" y1="0" x2="1" y2="1">
        <stop offset="0" stop-color="#f7f7f7"/>
        <stop offset="1" stop-color="#dcdcdc"/>
      </linearGradient>
      <linearGradient id="photoTone" x1="0" y1="0" x2="1" y2="1">
        <stop offset="0" stop-color="#9a9a9a"/>
        <stop offset=".55" stop-color="#4c4c4c"/>
        <stop offset="1" stop-color="#1e1e1e"/>
      </linearGradient>
      <linearGradient id="titlePanel" x1="0" y1="0" x2="1" y2="1">
        <stop offset="0" stop-color="#1f1f1f"/>
        <stop offset="1" stop-color="#343434"/>
      </linearGradient>
      <pattern id="dots2" width="4" height="4" patternUnits="userSpaceOnUse">
        <circle cx="2" cy="2" r="0.9" fill="#555"/>
      </pattern>
    </defs>
    <rect width="495" height="700" fill="url(#frontPaper)"/>

    <g class="masthead">
      <circle cx="45" cy="76" r="10" fill="none" stroke="var(--slate)" stroke-width="2"/>
      <text class="brand" x="68" y="84" font-size="23" fill="var(--slate)">The Heron Collective</text>
    </g>

    <rect class="dotted-strip" x="45" y="206" width="260" height="12" fill="url(#dots2)"/>

    <polygon class="diagonal-band" points="260,120 495,120 495,440 440,440 170,170" fill="var(--charcoal)"/>
    <polygon class="diagonal-band-light" points="360,120 495,120 495,260" fill="#555"/>

    <polygon class="cover-photo" role="img" aria-label="Photograph of colleagues silhouetted at a high office window overlooking a city"
      points="45,222 250,222 460,432 460,470 45,470" fill="url(#photoTone)"/>
    <polygon class="diagonal-band-lower" points="250,222 330,222 495,387 495,440 460,440" fill="var(--ink)" opacity=".85"/>

    <rect class="dotted-strip" x="300" y="450" width="195" height="12" fill="url(#dots2)"/>

    <g class="tile-cluster top" stroke="#e8e8e8" stroke-width="3">
      <rect x="330" y="150" width="42" height="42" fill="#3c3c3c" transform="rotate(45 351 171)"/>
      <rect x="362" y="182" width="42" height="42" fill="var(--ink)" transform="rotate(45 383 203)"/>
      <rect x="394" y="214" width="42" height="42" fill="#666" transform="rotate(45 415 235)"/>
    </g>
    <g class="tile-cluster lower" stroke="#e8e8e8" stroke-width="3">
      <rect x="195" y="410" width="36" height="36" fill="#3c3c3c" transform="rotate(45 213 428)"/>
      <rect x="222" y="437" width="36" height="36" fill="#777" transform="rotate(45 240 455)"/>
      <rect x="168" y="437" width="36" height="36" fill="var(--ink)" transform="rotate(45 186 455)"/>
    </g>

    <polygon class="title-panel" points="0,480 230,480 495,700 0,700" fill="url(#titlePanel)"/>
    <polygon class="title-panel-foot" points="0,640 495,640 495,700 0,700" fill="var(--ink)" opacity=".5"/>

    <g class="intro body" font-size="10" fill="#333" text-anchor="end">
      <text x="482" y="522">Most of our work is international</text>
      <text x="482" y="535">and we have a strong connection</text>
      <text x="482" y="548">to South Africa.</text>
    </g>
    <rect class="web-bar" x="345" y="566" width="150" height="20" fill="var(--ink)"/>
    <text class="body" x="358" y="580" font-size="10" fill="var(--white)">www.websiteaddress.com</text>

    <g class="cover-title heading" font-size="30" fill="var(--white)">
      <text x="30" y="575">SHORT ANNUAL</text>
      <text x="30" y="610">REVIEW FOR <tspan fill="var(--mist)">2016</tspan></text>
    </g>
    <g class="title-note body" font-size="8" fill="#888">
      <text x="30" y="632">The Heron Collective is a small public relations agency</text>
      <text x="30" y="643">in London specialising in corporate and public affairs.</text>
    </g>
  </svg>

</main>
</body>
</html>
```